Mireva Party Planning Brochure

I am beginning a new Party Planning business and need a brochure outlining my services. We are offering a full range of party/event-related planning services. These include Catering Halls/Restaurants, Photography/Video, International DJ's and Bands, Flowers, Tuxedos/Gowns, Limousines and Specialized Entertainers such as Clowns and Face Painters, Middle Eastern Belly Dancers, and Musical Impersonators (specifically, Dell Maronett impersonator). I would like a festive design, showing people having a good time in a festive setting. No vulgar or inappropriate photos or language, please.

Target Market(s)

Primarily, newly engaged couples. As for ethnic preference, Greek-speaking clientele.

Future brides, new parents and newly engaged couples, primarily in the Greek market.

Industry/Entity Type

Business

Font styles to use
Sans Serif

Colors
33a6d7

Requirements
Must have
• Mention of speaking Greek and Spanish. Festive design. I need to have this phrase included exactly as you see it
• I need the brochure to look, read and exude "happy".
Nice to have
• Pictures of party atmosphere. A lively room.
Should not have
• No vulgarities, no inappropriate pictures. No drunken photos or offensive images.

```html
<!DOCTYPE html>
<html lang="en">
<head>
<meta charset="utf-8">
<title>Mireva Party Planning Brochure</title>
<link href="https://fonts.googleapis.com/css2?family=Archivo:wght@700;800&family=Bitter:wght@700&display=swap" rel="stylesheet">
<style>
:root{
  --brand:#33a6d7;
  --brand-deep:#1d7fb3;
  --brand-soft:#5dbbe3;
  --band:#dff1fa;
  --ink:#111111;
  --paper:#ffffff;
}
*{box-sizing:border-box;margin:0;padding:0}
html,body{width:1200px;height:933px;overflow:hidden;background:var(--paper)}
.brochure{position:relative;width:1200px;height:933px;overflow:hidden}
.panel{position:absolute;top:0;height:933px}
.panel--cover-left{left:0;width:397px;background:var(--brand)}
.panel--services{left:397px;width:396px;background:var(--paper)}
.panel--photo{left:793px;width:407px;background:var(--brand)}
.photo-fill{position:absolute;left:0;top:0;width:407px;height:804px;
  background:linear-gradient(160deg,#1a6f9f 0%,#2f98cc 45%,#6ec4e8 75%,#2b8fc4 100%)}
.key-band{position:absolute;left:0;top:804px;width:1200px;height:48px;background:var(--band)}
.bottom-strip--services{position:absolute;left:397px;top:852px;width:396px;height:81px;background:var(--paper)}

.headline{position:absolute;left:62px;top:126px;font-family:'Archivo',sans-serif;font-weight:800;
  font-size:43px;line-height:49px;color:var(--paper);letter-spacing:.5px}

.wordmark{position:absolute;display:flex;align-items:center;gap:8px;font-family:'Archivo',sans-serif;font-weight:800;white-space:nowrap}
.wordmark .dot{border-radius:50%;flex:none}
.wordmark--left{left:168px;top:540px;font-size:17px;color:var(--paper)}
.wordmark--left .dot{width:14px;height:14px;background:var(--paper)}
.wordmark--services{left:500px;top:70px;width:200px;flex-direction:column;gap:6px;font-size:22px;color:var(--brand);text-align:center}
.wordmark--services .dot{width:64px;height:64px;background:var(--brand)}
.wordmark--photo{left:860px;top:130px;width:260px;flex-direction:column;gap:8px;font-size:26px;color:var(--paper);text-align:center}
.wordmark--photo .dot{width:84px;height:84px;background:var(--paper)}

.bubble{position:absolute;font-family:'Archivo',sans-serif;font-weight:700;border-radius:9px;line-height:1.05}
.bubble::after{content:"";position:absolute;bottom:-14px;width:0;height:0;border-left:8px solid transparent;border-right:8px solid transparent;border-top:14px solid currentColor}
.bubble--outline{border:2px solid var(--paper);color:var(--paper);background:transparent}
.bubble--fill{background:var(--brand);color:var(--paper);border:2px solid var(--paper)}
.bubble .label{color:var(--paper)}
.bubble--greek::after{left:18px}
.bubble--spanish::after{right:18px}

.bubble-left-greek{left:52px;top:630px;width:186px;height:74px;padding:9px 12px;font-size:24px;font-weight:700}
.bubble-left-spanish{left:198px;top:664px;width:146px;height:76px;padding:10px 14px;font-size:22px;background:var(--brand)}
.bubble-mid-greek{left:560px;top:541px;width:92px;height:40px;padding:4px 7px;font-size:13px;background:var(--brand);border-color:var(--brand)}
.bubble-mid-spanish{left:640px;top:564px;width:84px;height:38px;padding:4px 7px;font-size:12.5px;background:var(--brand);border-color:var(--paper)}
.bubble-photo-greek{left:866px;top:592px;width:184px;height:68px;padding:8px 12px;font-size:23px;background:#3aa7d8}
.bubble-photo-spanish{left:1006px;top:630px;width:152px;height:70px;padding:9px 14px;font-size:21px;background:var(--brand)}

.affiliates{position:absolute;left:397px;top:216px;width:396px;text-align:center;font-family:'Bitter',serif;font-weight:700;color:var(--ink)}
.affiliates h2{font-size:15.5px;line-height:19px;margin-bottom:18px}
.affiliates ul{list-style:none}
.affiliates li{font-size:15px;line-height:18px;margin-bottom:10px}
.affiliates li::before{content:"•";color:var(--brand);margin-right:12px}

.contact-lettering{position:absolute;left:468px;top:600px;width:244px;height:96px;border-radius:6px;
  background:linear-gradient(90deg,#d8eef8,#bfe3f4)}

.phone{position:absolute;font-family:'Bitter',serif;font-weight:700;letter-spacing:1px}
.phone--services{left:397px;top:708px;width:396px;text-align:center;font-size:27px;color:var(--ink)}
.phone--photo{left:793px;top:756px;width:407px;text-align:center;font-size:27px;color:var(--paper)}
.web{position:absolute;font-family:'Bitter',serif;font-weight:700}
.web--services{left:397px;top:750px;width:396px;text-align:center;font-size:14.5px;color:var(--ink)}
.web--photo{left:793px;top:865px;width:407px;text-align:center;font-size:16px;color:var(--paper)}
</style>
</head>
<body>
<main class="brochure">
  <section class="panel panel--cover-left">
    <h1 class="headline">Let Us<br>Make<br>Your<br>Special<br>Event<br>One That<br>Will Last<br>A Lifetime!</h1>
    <div class="wordmark wordmark--left"><span class="dot"></span><span>Mireva Party Planning</span></div>
    <div class="bubble bubble--outline bubble--greek bubble-left-greek">μιλαμε<br>ελλμνικα</div>
    <div class="bubble bubble--outline bubble--spanish bubble-left-spanish">Hablamos<br>Espanol</div>
  </section>

  <section class="panel panel--services"></section>
  <div class="wordmark wordmark--services"><span class="dot"></span><span>Mireva<br>Party Planning</span></div>
  <div class="affiliates">
    <h2>Mireva Party Planning is Affiliated<br>with the Best</h2>
    <ul>
      <li>Catering Halls &amp; Restaurants</li>
      <li>Photo &amp; Video</li>
      <li>International DJs &amp; Bands</li>
      <li>Limo Services</li>
      <li>Wedding Gowns<br>&amp; Bridesmaid Dresses</li>
      <li>Tuxedos</li>
      <li>Flowers</li>
      <li>Specialized Entertainers</li>
    </ul>
  </div>
  <div class="bubble bubble--fill bubble--greek bubble-mid-greek">μιλαμε<br>ελλμνικα</div>
  <div class="bubble bubble--fill bubble--spanish bubble-mid-spanish">Hablamos<br>Espanol</div>
  <div class="contact-lettering" role="img" aria-label="Hand-lettered Contact Us heading"></div>
  <p class="phone phone--services">(555) 214-0376</p>
  <p class="web web--services">www.mirevapartyplanning.com</p>

  <section class="panel panel--photo">
    <div class="photo-fill" role="img" aria-label="Blue-toned photo of a couple dancing at a festive wedding celebration"></div>
  </section>
  <div class="wordmark wordmark--photo"><span class="dot"></span><span>Mireva<br>Party Planning</span></div>
  <div class="bubble bubble--outline bubble--greek bubble-photo-greek">μιλαμε<br>ελλμνικα</div>
  <div class="bubble bubble--outline bubble--spanish bubble-photo-spanish">Hablamos<br>Espanol</div>
  <p class="phone phone--photo">(555) 214-0376</p>

  <div class="key-band" role="img" aria-label="Greek key meander border band"></div>
  <div class="bottom-strip--services"></div>
  <p class="web web--photo">www.mirevapartyplanning.com</p>
</main>
</body>
</html>
```